Brackwell HVAC Service LLC Business Card

We just got a design created by one of your designers for a logo and now would like help with a business card design. The information to be included on the card is as follows:
Brackwell HVAC Service LLC (I will attach logo design)
P.O. Box 418
Halden, CO 80694
(970) 555-0147
Dale Vonnholt
I might include an e-mail address, but I'm not sure yet.
Target Market(s)
Customers needing service or repairs done on their heating and air conditioning systems.
Industry/Entity Type
Business
Contact Information for Business Card
P.O. Box 418
Halden, CO 80694
(970) 555-0147
Dale Vonnholt

```html
<!DOCTYPE html>
<html lang="en">
<head>
<meta charset="utf-8">
<title>Brackwell HVAC Service LLC – Business Card</title>
<link rel="stylesheet" href="https://fonts.googleapis.com/css2?family=Jost:wght@400;600&display=swap">
<style>
  :root {
    --backdrop: #8e8e8e;
    --card-white: #f3f3f3;
    --navy: #102a56;
    --red: #c0161f;
    --text-light: #e6e8ec;
    --divider: #c9ced8;
  }
  html, body {
    margin: 0;
    padding: 0;
    width: 1200px;
    height: 840px;
    overflow: hidden;
    background: var(--backdrop);
    font-family: "Jost", "Futura", sans-serif;
  }
  .canvas {
    position: relative;
    width: 1200px;
    height: 840px;
  }
  .card {
    position: absolute;
    left: 75px;
    top: 120px;
    width: 1050px;
    height: 600px;
    background: var(--navy);
    overflow: hidden;
    box-shadow: 0 12px 30px rgba(0,0,0,0.25);
  }
  .card-shapes {
    position: absolute;
    inset: 0;
  }
  .card-shapes .white { fill: var(--card-white); }
  .card-shapes .red { fill: var(--red); }
  .brand {
    position: absolute;
    left: 56px;
    top: 70px;
    display: flex;
    align-items: center;
    gap: 18px;
  }
  .brand-dot {
    width: 44px;
    height: 44px;
    border-radius: 50%;
    background: var(--red);
  }
  .brand-name {
    font-weight: 600;
    font-size: 40px;
    color: var(--navy);
    letter-spacing: 0.5px;
    margin: 0;
  }
  .person-name {
    position: absolute;
    left: 60px;
    top: 345px;
    margin: 0;
    font-weight: 400;
    font-size: 60px;
    letter-spacing: 1px;
    color: var(--text-light);
  }
  .contact {
    position: absolute;
    display: flex;
    align-items: center;
    gap: 14px;
    color: var(--text-light);
    font-size: 28px;
    line-height: 1.2;
  }
  .contact .icon {
    width: 32px;
    height: 32px;
    fill: var(--text-light);
  }
  .contact .rule {
    width: 2px;
    align-self: stretch;
    background: var(--divider);
  }
  .contact-address { left: 60px; top: 455px; }
  .contact-phone { left: 560px; top: 338px; }
  .contact-phone .rule { height: 52px; }
</style>
</head>
<body>
<div class="canvas">
  <div class="card">
    <svg class="card-shapes" viewBox="0 0 1050 600" width="1050" height="600" aria-hidden="true">
      <path class="white" d="M0 0 H1050 V117 C820 200 420 310 0 342 Z"/>
      <path class="red" d="M0 0 H1050 V111 C820 194 420 304 0 336 Z"/>
      <path class="white" d="M0 0 H1050 V95 C820 178 420 288 0 320 Z"/>
    </svg>

    <div class="brand">
      <div class="brand-dot"></div>
      <p class="brand-name">Brackwell HVAC Service LLC</p>
    </div>

    <h1 class="person-name">Dale Vonnholt</h1>

    <div class="contact contact-address">
      <svg class="icon" viewBox="0 0 24 24" aria-hidden="true">
        <path d="M12 3 L2 12 H5 V21 H10 V15 H14 V21 H19 V12 H22 Z"/>
      </svg>
      <span class="rule"></span>
      <div class="address-lines">P.O. Box 418<br>Halden, CO 80694</div>
    </div>

    <div class="contact contact-phone">
      <svg class="icon" viewBox="0 0 24 24" aria-hidden="true">
        <path d="M3 9 C3 6 7 5 12 5 C17 5 21 6 21 9 V10 H16 V8.5 C14.5 8 9.5 8 8 8.5 V10 H3 Z"/>
        <path d="M7 11 H17 L19 19 H5 Z"/>
      </svg>
      <span class="rule"></span>
      <span class="phone-number">(970) 555-0147</span>
    </div>
  </div>
</div>
</body>
</html>
```